Premium Landcaping Vehicle Design; for 7 vehicles.

Goal: Designs for all of our landscaping vehicles that are bold, premium, visually appealing, and effectively communicate our brand/service while being practical for a vehicle and the damage it could potentially get from tools etc.
1. Brand Identity:
Logo: Feature our logo prominently but ensure it doesn’t overwhelm the design. It should be visible from a distance.
2. Layout:
Simplicity: The car wrap should not be overcrowded. Less is more in mobile advertising since people have only seconds to take it in.
Flow: Make sure the design flows with the curves and shape of the vehicle, using lines that move smoothly over the contours.
Small truck
Large Truck
Kelso Tarvin
Small trailer
Posi Truck
Plant Trailer
Boxtop trailer
Updates
Thank you for all the great ideas/ designs. After look at them all. I thought it would be great to see the ute tarvin have less colour; make it more of a premium look by trying the primary logo on one door and another design over both doors to make it stand out.
The truck - we don't want any block colour over the whole tray of the truck, just the bottom part of this, please. No need for website on the cars, ideally we would prefer Brantmoor and contact number to stand out.
Would also be great to see the body of the truck (sides only) all in green; making the colour fade down from the top of the door to the bottom/ near the wheel? So the whole side is green.
Hi all,
I have attached our AI logo's to ensure we're seeing the correct logo on the designs; meaning font, size of the wording etc. Would be great to see the correct logo on the design.
Thank you

```html
<!DOCTYPE html>
<html lang="en">
<head>
<meta charset="utf-8">
<title>Brantmoor Landscapes – Kelso Tarvin Wrap</title>
<link rel="stylesheet" href="https://fonts.googleapis.com/css2?family=Barlow+Condensed:wght@600&family=Exo+2:ital,wght@1,900&family=Poppins:wght@300&family=Roboto+Condensed:ital,wght@1,600&display=swap">
<style>
  :root {
    --forest: #112b1e;
    --mint: #7df09f;
    --mint-pale: #dcfbe5;
    --tyre: #000000;
    --hub: #3c3c3c;
    --trim: #1a1a1a;
    --lamp: #ff0000;
    --paper: #ffffff;
  }
  html, body {
    margin: 0;
    width: 1200px;
    height: 848px;
    overflow: hidden;
    background: var(--paper);
  }
  .sheet { display: block; width: 1200px; height: 848px; }
  .body-dark { fill: var(--forest); }
  .trim { fill: var(--trim); }
  .tyre { fill: var(--tyre); }
  .hub { fill: var(--hub); }
  .lamp { fill: var(--lamp); }
  .light { fill: var(--mint-pale); }
  .mint { fill: var(--mint); }
  .panel-line { fill: none; stroke: var(--tyre); stroke-width: 1.5; }
  .belt-line { fill: none; stroke: var(--tyre); stroke-width: 1; opacity: 0.6; }
  .handle { fill: var(--forest); stroke: var(--tyre); stroke-width: 5; }
  .tagline {
    font-family: "Barlow Condensed", sans-serif;
    font-weight: 600;
    font-size: 27px;
    fill: var(--paper);
  }
  .phone {
    font-family: "Exo 2", sans-serif;
    font-style: italic;
    font-weight: 900;
    font-size: 26px;
    fill: var(--forest);
  }
  .web {
    font-family: "Roboto Condensed", sans-serif;
    font-style: italic;
    font-weight: 600;
    font-size: 14px;
    fill: var(--forest);
  }
  .brand-name {
    font-family: "Poppins", sans-serif;
    font-weight: 300;
    font-size: 22px;
    letter-spacing: 3px;
    fill: var(--paper);
  }
  .brand-mark { fill: var(--paper); }
  .tailgate-name {
    font-family: "Poppins", sans-serif;
    font-weight: 300;
    font-size: 62px;
    letter-spacing: 10px;
    fill: var(--forest);
  }
  .tailgate-phone {
    font-family: "Exo 2", sans-serif;
    font-style: italic;
    font-weight: 900;
    font-size: 38px;
    fill: var(--paper);
  }
</style>
</head>
<body>
<svg class="sheet" viewBox="0 0 2339 1654" xmlns="http://www.w3.org/2000/svg" role="img" aria-label="Brantmoor Landscapes wrap for the Kelso Tarvin ute: driver side, passenger side and rear">
  <defs>
    <linearGradient id="side-fade" x1="0" y1="0" x2="1" y2="0">
      <stop offset="0" stop-color="var(--forest)"/>
      <stop offset="0.25" stop-color="#2f7a4c"/>
      <stop offset="0.55" stop-color="var(--mint)"/>
      <stop offset="1" stop-color="var(--mint)"/>
    </linearGradient>
    <linearGradient id="panel-fade" x1="0" y1="0" x2="1" y2="0">
      <stop offset="0" stop-color="var(--mint-pale)"/>
      <stop offset="1" stop-color="#f4fff7"/>
    </linearGradient>
    <linearGradient id="glass" x1="0" y1="0" x2="1" y2="0">
      <stop offset="0" stop-color="#e8e8e8"/>
      <stop offset="0.45" stop-color="#8a8a8a"/>
      <stop offset="1" stop-color="#0d0d0d"/>
    </linearGradient>
    <linearGradient id="cab-shade" x1="0" y1="0" x2="0" y2="1">
      <stop offset="0" stop-color="var(--forest)"/>
      <stop offset="1" stop-color="#3f9a60"/>
    </linearGradient>

    <g id="ute-side">
      <!-- body shell -->
      <path class="body-dark" d="M130,555 L140,490 Q160,458 195,450 Q330,422 445,420 L610,330 Q690,312 900,312 L985,320 Q1012,335 1015,420 L1395,418 Q1415,425 1418,455 L1418,585 L1360,590 L1350,640 L1250,650 L440,668 L150,660 Z"/>
      <path fill="url(#cab-shade)" d="M965,330 Q995,335 1000,420 L1015,420 Q1012,335 985,320 Z"/>
      <!-- fading side sweep -->
      <path fill="url(#side-fade)" d="M690,442 L985,434 L1012,490 L1418,488 L1418,570 L1255,580 L1250,648 L812,648 Z"/>
      <!-- pale contact panel -->
      <path fill="url(#panel-fade)" d="M760,490 L978,490 L965,562 L840,592 L870,648 L835,648 Z"/>
      <!-- tray top band -->
      <path class="body-dark" d="M1005,438 L1410,436 L1418,488 L1012,490 Z"/>
      <!-- glass -->
      <path fill="url(#glass)" d="M505,447 Q545,360 650,342 L935,340 Q960,345 962,400 Q958,428 930,432 Z"/>
      <path class="panel-line" d="M748,340 L735,440 M770,340 L768,435 M750,437 L760,640 M985,430 L965,650"/>
      <!-- belt line, kept within the doors -->
      <path class="belt-line" d="M495,575 L970,565"/>
      <!-- mirror -->
      <path class="tyre" d="M515,400 Q540,392 560,398 Q568,420 565,438 Q550,452 525,450 Q505,440 512,420 Z"/>
      <!-- handles -->
      <rect class="handle" x="670" y="470" width="65" height="12" rx="6"/>
      <rect class="handle" x="898" y="462" width="65" height="12" rx="6"/>
      <!-- headlight -->
      <path class="light" d="M150,492 L228,481 Q245,482 233,497 Q212,522 190,527 L147,533 Z"/>
      <!-- grille vent -->
      <path class="trim" d="M425,475 L485,470 L490,498 L445,498 Z"/>
      <!-- tail lamp -->
      <path class="lamp" d="M1372,462 L1420,462 L1420,565 L1385,565 Q1368,540 1368,505 Z"/>
      <!-- front bumper, joined to the body -->
      <path class="trim" d="M130,555 L140,548 L225,565 L222,662 L185,664 Q160,660 140,645 L132,620 Q128,590 130,555 Z"/>
      <!-- rear bumper, joined to the body -->
      <path class="trim" d="M1355,588 L1418,585 L1436,583 Q1448,588 1446,602 L1441,628 Q1434,648 1412,650 L1250,660 L1250,645 L1350,640 Z"/>
      <!-- sill -->
      <path class="trim" d="M430,652 L1250,645 L1250,680 L430,680 Z"/>
      <!-- wheels -->
      <circle class="trim" cx="335" cy="652" r="138"/>
      <circle class="tyre" cx="335" cy="652" r="104"/>
      <circle class="hub" cx="335" cy="652" r="67"/>
      <circle class="tyre" cx="335" cy="652" r="29"/>
      <circle class="trim" cx="1140" cy="652" r="135"/>
      <circle class="tyre" cx="1140" cy="652" r="104"/>
      <circle class="hub" cx="1140" cy="652" r="67"/>
      <circle class="tyre" cx="1140" cy="652" r="29"/>
    </g>
  </defs>

  <!-- driver side -->
  <g class="view view-driver">
    <use href="#ute-side"/>
    <text class="tagline" x="1053" y="472">DESIGN. CONSTRUCT. MAINTAIN</text>
    <text class="phone" x="798" y="520">0400 555 219</text>
    <text class="web" x="812" y="546">brantmoorlandscaping.au</text>
    <rect class="brand-mark" x="600" y="515" width="40" height="40"/>
    <text class="brand-name" x="620" y="598" text-anchor="middle">BRANTMOOR</text>
  </g>

  <!-- passenger side -->
  <g class="view view-passenger">
    <use href="#ute-side" transform="translate(1570,555) scale(-1,1)"/>
    <text class="tagline" x="218" y="1035">DESIGN. CONSTRUCT. MAINTAIN</text>
    <text class="phone" x="603" y="1075">0400 555 219</text>
    <text class="web" x="612" y="1100">brantmoorlandscaping.au</text>
    <rect class="brand-mark" x="928" y="1070" width="40" height="40"/>
    <text class="brand-name" x="948" y="1153" text-anchor="middle">BRANTMOOR</text>
  </g>

  <!-- rear -->
  <g class="view view-rear">
    <path fill="none" stroke="var(--tyre)" stroke-width="10" d="M1625,640 L1625,628 L1565,630 Q1540,635 1540,660 L1540,700 L1620,698 Z"/>
    <path fill="none" stroke="var(--tyre)" stroke-width="10" d="M2175,640 L2175,628 L2235,630 Q2260,635 2262,660 L2262,700 L2180,698 Z"/>
    <rect class="tyre" x="1740" y="505" width="20" height="18"/>
    <rect class="tyre" x="2080" y="505" width="20" height="18"/>
    <path class="body-dark" d="M1650,690 L1705,540 Q1712,520 1738,520 L2098,520 Q2118,520 2126,540 L2180,690 Z"/>
    <path fill="none" stroke="var(--tyre)" stroke-width="2" d="M1680,665 L1725,565 Q1732,552 1750,552 L2085,552 Q2102,552 2110,565 L2155,655 Q2158,675 2140,677 L1690,677 Q1675,675 1680,665 Z"/>
    <rect class="trim" x="1855" y="543" width="122" height="18" rx="3"/>
    <rect class="lamp" x="1865" y="549" width="102" height="6"/>
    <rect class="brand-mark" x="1895" y="588" width="36" height="36"/>
    <path class="mint" d="M1585,725 Q1590,688 1625,686 L2210,686 Q2245,690 2250,725 L2250,885 L1585,885 Z"/>
    <rect class="body-dark" x="1585" y="808" width="665" height="52"/>
    <rect class="light" x="1592" y="698" width="48" height="32"/>
    <rect class="light" x="2197" y="698" width="48" height="32"/>
    <rect class="tyre" x="1862" y="720" width="106" height="24"/>
    <text class="tailgate-name" x="1918" y="802" text-anchor="middle">BRANTMOOR</text>
    <text class="tailgate-phone" x="1910" y="852" text-anchor="middle">0400 555 219</text>
    <rect class="lamp" x="1590" y="740" width="48" height="145"/>
    <rect class="lamp" x="2202" y="740" width="48" height="145"/>
    <path class="trim" d="M1585,885 L2250,885 L2250,940 Q2248,955 2240,960 Q2250,970 2250,1000 L2250,1060 Q2248,1072 2238,1072 L2150,1072 L2142,1040 L1985,1040 Q1960,1075 1915,1078 Q1870,1075 1845,1040 L1690,1040 L1680,1072 L1590,1072 Q1580,1070 1580,1060 L1580,1000 Q1580,970 1590,960 Q1583,950 1585,935 Z"/>
    <rect class="light" x="1592" y="892" width="48" height="20" rx="3"/>
    <rect class="light" x="2202" y="892" width="48" height="20" rx="3"/>
    <rect fill="var(--paper)" stroke="var(--tyre)" stroke-width="4" x="1812" y="898" width="210" height="55" rx="6"/>
    <rect class="tyre" x="1597" y="1072" width="83" height="80" rx="4"/>
    <rect class="tyre" x="2160" y="1072" width="83" height="80" rx="4"/>
  </g>
</svg>
</body>
</html>
```